Commercial Construction Company

We need a business card design based on our current logo. We are a commercial general contractor based in Southern California that specializes in bank remodels. We would like to see designs that incorporate dark blue. The final design should portray an image of professionalism and quality.

If possible, I would like to add metallic foil to the design. Thank you

```html
<!DOCTYPE html>
<html lang="en">
<head>
<meta charset="utf-8">
<title>Harlow Civic Builders – Business Card</title>
<link href="https://fonts.googleapis.com/css2?family=Open+Sans:wght@400;700&display=swap" rel="stylesheet">
<style>
  :root {
    --page-bg: #e4e3e1;
    --navy-top: #2f6198;
    --navy-bottom: #144a82;
    --card-white: #ffffff;
    --band-grey: #a7a7a7;
    --ink: #1b1b1b;
    --charcoal-top: #3a3b3d;
    --charcoal-bottom: #1e1f21;
    --foil: #b9b9bb;
    --edge-blue: #1d4f8a;
  }
  html, body {
    margin: 0;
    width: 1200px;
    height: 801px;
    overflow: hidden;
    background: var(--page-bg);
    font-family: "Open Sans", sans-serif;
  }
  .stage {
    position: relative;
    width: 1200px;
    height: 801px;
  }
  .card {
    position: absolute;
    top: 258px;
    width: 500px;
    height: 286px;
    border-radius: 3px;
    overflow: hidden;
    box-shadow: 0 10px 24px rgba(0,0,0,0.18), 0 2px 0 var(--edge-blue);
  }
  .card--front { left: 70px; }
  .card--back {
    left: 630px;
    background: linear-gradient(160deg, var(--charcoal-top), var(--charcoal-bottom));
  }
  .front-art {
    position: absolute;
    inset: 0;
  }
  .wordmark {
    position: absolute;
    display: flex;
    align-items: center;
    gap: 8px;
    font-weight: 700;
    letter-spacing: 0.06em;
    white-space: nowrap;
  }
  .wordmark__dot {
    border-radius: 50%;
    flex: none;
  }
  .card--front .wordmark {
    left: 275px;
    top: 78px;
    font-size: 15px;
    color: var(--ink);
  }
  .card--front .wordmark__dot {
    width: 14px;
    height: 14px;
    background: var(--navy-bottom);
  }
  .card--back .wordmark {
    left: 50%;
    top: 50%;
    transform: translate(-50%, -50%);
    font-size: 26px;
    color: var(--foil);
  }
  .card--back .wordmark__dot {
    width: 22px;
    height: 22px;
    background: var(--foil);
  }
  .contact {
    position: absolute;
    left: 26px;
    top: 112px;
    color: var(--card-white);
  }
  .contact__name {
    margin: 0;
    font-size: 17px;
    font-weight: 700;
    letter-spacing: 0.02em;
    text-transform: uppercase;
  }
  .contact__role {
    margin: 0 0 12px;
    font-size: 12.5px;
  }
  .contact__address {
    margin: 0 0 10px;
    font-size: 12px;
    font-style: normal;
    line-height: 1.35;
  }
  .contact__list {
    list-style: none;
    margin: 0;
    padding: 0;
    font-size: 12px;
    line-height: 1.45;
  }
  .contact__list li {
    display: flex;
    align-items: center;
    gap: 7px;
  }
  .contact__icon {
    width: 10px;
    height: 10px;
    flex: none;
  }
</style>
</head>
<body>
<main class="stage">

  <section class="card card--front" aria-label="Business card front">
    <svg class="front-art" viewBox="0 0 500 286" width="500" height="286" aria-hidden="true">
      <defs>
        <linearGradient id="navyFill" x1="0" y1="0" x2="0" y2="1">
          <stop offset="0" stop-color="#2f6198"/>
          <stop offset="1" stop-color="#144a82"/>
        </linearGradient>
      </defs>
      <rect width="500" height="286" fill="url(#navyFill)"/>
      <circle cx="388" cy="44" r="200" fill="#ffffff"/>
      <circle cx="380" cy="54" r="192" fill="#a7a7a7"/>
      <circle cx="392" cy="40" r="188" fill="#ffffff"/>
    </svg>

    <div class="wordmark">
      <span class="wordmark__dot"></span>
      <span>HARLOW CIVIC</span>
    </div>

    <div class="contact">
      <h1 class="contact__name">Marcus Delane</h1>
      <p class="contact__role">Founder &amp; CEO</p>
      <address class="contact__address">418 Harbor Point, Suite #210<br>Oceanside, CA 92054</address>
      <ul class="contact__list">
        <li>
          <svg class="contact__icon" viewBox="0 0 10 10" aria-hidden="true"><path d="M2 1 L4 1 L4.6 3 L3.4 4 Q4.3 5.8 6 6.6 L7 5.4 L9 6 L9 8 Q8.5 9 7.5 9 Q1 8.2 1 2.5 Q1 1.5 2 1Z" fill="#fff"/></svg>
          (555) 010 2468
        </li>
        <li>
          <svg class="contact__icon" viewBox="0 0 10 10" aria-hidden="true"><rect x="0.5" y="2" width="9" height="6.5" fill="none" stroke="#fff"/><path d="M0.5 2 L5 5.6 L9.5 2" fill="none" stroke="#fff"/></svg>
          hello@harlowcivic.com
        </li>
        <li>
          <svg class="contact__icon" viewBox="0 0 10 10" aria-hidden="true"><circle cx="5" cy="5" r="4.3" fill="none" stroke="#fff"/><ellipse cx="5" cy="5" rx="1.9" ry="4.3" fill="none" stroke="#fff" stroke-width="0.8"/><path d="M0.7 5 H9.3" stroke="#fff" stroke-width="0.8"/></svg>
          www.harlowcivic.com
        </li>
      </ul>
    </div>
  </section>

  <section class="card card--back" aria-label="Business card back">
    <div class="wordmark">
      <span class="wordmark__dot"></span>
      <span>HARLOW CIVIC</span>
    </div>
  </section>

</main>
</body>
</html>
```